CoinLantern one-page corporate website

Our company, CoinLantern is a cryptocurrency Initial Coin Offering ("ICO" marketing and promotion agency, which requires a professional company landing page design whereby prospective clients can learn;
-who we are
-what we do
-what our people are saying about us
-core team members
-subscribe to our mailing list
-how to get in touch (basic contact form)

We are looking for something unique and attractive -- not a standard Pako template that we could put together ourselves. Plain stock images should not be used. Unique visualizations of the service offerings and creative presentation are key. We are a cutting edge marketing agency and as such, we need to look the part.

Relevant documentation about the business and branding assets have been attached to guide the designer. Certain information will be included by the company at a later date such as team member descriptions. As such, lorem ipsum may be included wherever necessary to help visualize the textual areas.

****Please ensure that you actually utilize the photos and graphics provided so that we can have a good picture of what it would actually look like with our branding.

The site must be responsive HTML CSS Design.

Sites style themes we like for inspiration and specific sections we like ****Very important***:
https://vaultorbitra.example/offers - we like that the token & company logo is used in unique visualizations that connects various ideas together. We imagine unique visuals such as these with our Icon (see attached) serving as a token. We also like the unique and attractive visual theme of the webpage itself.

https://quarrelstone.example/ - we like the layout of this website, specifically how the service offerings are displayed in a circular visual graphic with the Quarrel logo in the middle. We imagine a similar type of graphic designed with CoinLantern in the middle.

https://zorvinet.example/ - we like how the logo is central to the theme in this site when you first enter and how it fades + shrinks into the distance as you scroll down.

Target Market(s)

cryptocurrency entrepreneurs and ICOs

Industry/Entity Type

It Company

Coding

Coded - Design and coding required

Number of Pages Required

1 page

Font styles to use
Sans Serif

Colors

Designer to choose colors to be used in the design.

Requirements
Must have
• The site must be responsive HTML CSS Design.
• The page must be modern and visually attractive. Elements must not be static and should have a fluid motion / visual change as the user scrolls through the page.
Should not have
• The project should not use any old stock images or elements which are dull and over-used, but rather images or elements should be unique and well thought out.

```html
<!DOCTYPE html>
<html lang="en">
<head>
<meta charset="UTF-8">
<title>CoinLantern — Token Launch Advisors</title>
<link href="https://fonts.googleapis.com/css2?family=Poppins:wght@300;400;500;700&display=swap" rel="stylesheet">
<style>
  :root {
    --hero-deep: #1d3c62;
    --hero-mid: #2e5682;
    --hero-light: #3d6a96;
    --ink-light: #ffffff;
  }
  * { margin: 0; padding: 0; box-sizing: border-box; }
  html, body { width: 1200px; height: 659px; overflow: hidden; }
  body { font-family: 'Poppins', sans-serif; color: var(--ink-light); background: var(--hero-deep); }

  .hero { position: relative; width: 1200px; height: 659px; overflow: hidden; }
  .hero-backdrop {
    position: absolute; inset: 0;
    background: radial-gradient(ellipse at 55% 60%, var(--hero-light) 0%, var(--hero-mid) 45%, var(--hero-deep) 100%);
  }

  .site-header { position: absolute; top: 0; left: 0; width: 100%; height: 96px; }
  .brand { position: absolute; left: 132px; top: 18px; display: flex; align-items: center; }
  .brand-mark { width: 50px; height: 50px; border: 2.5px solid var(--ink-light); border-radius: 50%; }
  .brand-text { margin-left: 8px; display: flex; flex-direction: column; align-items: flex-start; }
  .brand-name { font-weight: 500; font-size: 26px; line-height: 30px; letter-spacing: 0.5px; }
  .brand-tagline { font-weight: 500; font-size: 10.5px; line-height: 14px; }

  .main-nav { position: absolute; top: 38px; left: 468px; display: flex; }
  .nav-link {
    display: flex; align-items: center; gap: 6px;
    color: var(--ink-light); text-decoration: none;
    font-size: 14.5px; font-weight: 400; line-height: 20px; margin-right: 27px;
  }
  .nav-link svg { width: 14px; height: 14px; fill: var(--ink-light); }

  .hero-copy { position: absolute; top: 300px; left: 0; width: 100%; text-align: center; }
  .hero-kicker { font-weight: 300; font-size: 35.5px; line-height: 46px; }
  .hero-title { font-weight: 700; font-size: 36px; line-height: 54px; letter-spacing: -0.5px; margin-top: 6px; }

  .cta {
    position: absolute; left: 514px; top: 520px; width: 172px; height: 36px;
    border: 1.2px solid var(--ink-light); border-radius: 18px;
    display: flex; align-items: center; justify-content: center; gap: 6px;
    color: var(--ink-light); text-decoration: none; font-size: 14px; font-weight: 400;
  }
  .cta svg { width: 10px; height: 10px; }

  .slider-dots { position: absolute; top: 608px; left: 571px; display: flex; gap: 5.5px; }
  .dot { width: 16px; height: 16px; border: 1.2px solid var(--ink-light); border-radius: 50%; position: relative; }
  .dot.is-active::after {
    content: ""; position: absolute; left: 4px; top: 4px; width: 6px; height: 6px;
    background: var(--ink-light); border-radius: 50%;
  }
</style>
</head>
<body>
<section class="hero">
  <div class="hero-backdrop" role="img" aria-label="Close-up photo of stacked chips, tinted deep blue"></div>

  <header class="site-header">
    <div class="brand">
      <span class="brand-mark"></span>
      <div class="brand-text">
        <span class="brand-name">CoinLantern</span>
        <span class="brand-tagline">Token Launch Advisors</span>
      </div>
    </div>

    <nav class="main-nav">
      <a class="nav-link" href="#home">
        <svg viewBox="0 0 16 16"><path d="M8 1.5 0.5 8h2v6.5h4.2v-4.2h2.6v4.2h4.2V8h2z"/></svg>HOME
      </a>
      <a class="nav-link" href="#about" style="margin-left:8px">
        <svg viewBox="0 0 16 16"><circle cx="8" cy="2.5" r="1.8"/><path d="M5.5 6h4v7.5h1.5V15h-6v-1.5H7V7.5H5.5z"/></svg>ABOUT
      </a>
      <a class="nav-link" href="#testimonials">
        <svg viewBox="0 0 16 16"><path d="M1 8.5C1 5 2.5 3 6 2.5v2C4.3 5 3.6 6 3.5 7.5H7V14H1zM9 8.5C9 5 10.5 3 14 2.5v2c-1.7.5-2.4 1.5-2.5 3H15V14H9z"/></svg>TESTIMONIALS
      </a>
      <a class="nav-link" href="#team">
        <svg viewBox="0 0 16 16"><circle cx="8" cy="4.5" r="2.5"/><circle cx="3" cy="5.5" r="1.8"/><circle cx="13" cy="5.5" r="1.8"/><path d="M3.5 14c0-3 2-5 4.5-5s4.5 2 4.5 5zM0 12.5C0 10 1.3 8.5 3 8.5c.7 0 1.2.2 1.6.5C3.6 10 3 11.2 2.9 12.5zM16 12.5c0-2.5-1.3-4-3-4-.7 0-1.2.2-1.6.5 1 1 1.6 2.200 1.7 3.5z"/></svg>TEAM
      </a>
      <a class="nav-link" href="#contact">
        <svg viewBox="0 0 16 16"><path d="M1 3h14v1.5L8 9 1 4.5z"/><path d="M1 6.3 8 10.8l7-4.5V13H1z"/></svg>CONTACT
      </a>
    </nav>
  </header>

  <div class="hero-copy">
    <p class="hero-kicker">A FULL-SERVICE INVESTMENT BANK FOR</p>
    <h1 class="hero-title">THE DIGITAL TOKEN CAPITAL MARKETS</h1>
  </div>

  <a class="cta" href="#about">KNOW MORE
    <svg viewBox="0 0 10 10" fill="none" stroke="#ffffff" stroke-width="1.6"><path d="M1.5 1.5 5 5l3.5-3.5M1.5 5.5 5 9l3.5-3.5"/></svg>
  </a>

  <div class="slider-dots">
    <span class="dot is-active"></span>
    <span class="dot"></span>
    <span class="dot"></span>
  </div>
</section>
</body>
</html>
```